Occupational Therapy Needs an eye catching brochure for new business

I need a brochure for a new business that would be eye catching. I am an occupational therapist and this business will specifically deal with auditory processing delays and visual processing delays.If the childs delays stem from unintegrated reflexes that will be dealt with,as well. I have attached a brochure that I created. After having created it I decided that I wanted to seek professional graphics artist to help create an eye catching brochure that would attract more attention then my current unprofessional one. The attached brochures backgrounds should be changed. The wording should be changed and be more professionalized but the message should stay. I do not have a logo, since I am new, so you can create one for me, as well.

Please keep it a tri-fold. I have added the original brother file .edit and a word document with my text inside. Please give the brochure a professional look. I want those seeing my brochure to get the feel that my therapy business is a very professional and experienced business.Thank You Added Sunday, April 26, 2015

Parents of children with learning delays, whom are struggling and not getting good grades in school.

• Please keep it a tri-fold brochure
• Please include on the front page the following questions, they can be worded differently:
• Does your child have difficulty learning ABC and /or aleph bet?
• Does your child know the information for the test and does not do well on the test?
• Does your child have difficulty remembering name and dates in school, for test, or every day life?
• Please do not include pictures of Adults in the brochure.

```html
<!DOCTYPE html>
<html lang="en">
<head>
<meta charset="utf-8">
<title>Bright Path OT Services – Tri-fold Brochure</title>
<link rel="stylesheet" href="https://fonts.googleapis.com/css2?family=Roboto:wght@300;400;500;700&display=swap">
<style>
  :root {
    --stage: #3b3b3b;
    --paper: #ffffff;
    --orange: #f5822a;
    --blue: #5cb0e2;
    --green: #7ab32e;
    --ink: #222222;
    --ink-soft: #3a3a3a;
    --photo-warm-a: #f3d9c4;
    --photo-warm-b: #c98f6a;
    --photo-cool-a: #dfe9f2;
    --photo-cool-b: #8fb2cf;
  }
  * { box-sizing: border-box; margin: 0; padding: 0; }
  html, body { width: 754px; height: 1200px; overflow: hidden; }
  body {
    background: var(--stage);
    font-family: "Roboto", Arial, sans-serif;
    color: var(--ink);
  }
  .sheet {
    position: absolute;
    left: 32px;
    width: 690px;
    height: 540px;
    display: flex;
    background: var(--paper);
    box-shadow: 0 8px 22px rgba(0,0,0,.45);
  }
  .sheet--outside { top: 30px; }
  .sheet--inside { top: 625px; }
  .panel {
    width: 230px;
    height: 100%;
    display: flex;
    flex-direction: column;
    position: relative;
    border-right: 1px solid #e6e6e6;
    text-align: center;
    overflow: hidden;
  }
  .panel:last-child { border-right: none; }

  /* outside */
  .band-orange {
    background: var(--orange);
    color: #fff;
    height: 95px;
    flex: none;
    padding: 14px 12px;
  }
  .brand { text-align: left; padding-top: 18px; }
  .brand__name {
    font-size: 23px; font-weight: 700; letter-spacing: .5px; line-height: 1;
    display: flex; align-items: center; gap: 6px;
  }
  .brand__dot { width: 12px; height: 12px; border-radius: 50%; background: #fff; display: inline-block; }
  .brand__sub { font-size: 15px; font-weight: 700; margin-top: 5px; }
  .intro { font-size: 11px; padding: 12px 12px 6px; line-height: 1.35; color: var(--ink-soft); }
  .intro-lead { font-size: 18px; line-height: 1.2; padding: 0 12px; }
  .questions {
    list-style: none;
    text-align: left;
    padding: 10px 14px 0;
    font-size: 9.5px;
    line-height: 1.35;
    color: var(--ink-soft);
  }
  .questions li { position: relative; padding-left: 12px; margin-bottom: 5px; }
  .questions li::before {
    content: ""; position: absolute; left: 0; top: 4px;
    width: 6px; height: 6px; border-radius: 50%; background: var(--orange);
  }
  .photo { flex: 1; margin-top: 6px; }
  .photo--warm { background: linear-gradient(180deg, var(--photo-warm-a), var(--photo-warm-b)); }
  .photo--cool { background: linear-gradient(180deg, var(--photo-cool-a), var(--photo-cool-b)); }
  .photo--top { flex: none; height: 165px; margin: 0; }
  .photo--small { flex: none; height: 120px; width: 120px; margin: auto auto 18px; border-radius: 4px; }
  .photo--corner { flex: none; height: 170px; width: 140px; margin: auto 0 0 auto; }

  .question { color: var(--green); font-weight: 700; font-size: 12px; line-height: 1.35; padding: 12px 14px 10px; }
  .body { font-size: 10.5px; line-height: 1.4; padding: 0 14px; color: var(--ink-soft); }
  .body p + p { margin-top: 10px; }
  .caption { font-weight: 700; font-size: 10.5px; margin-top: 18px; text-transform: uppercase; color: var(--ink); }

  .contact { list-style: none; text-align: left; padding-top: 6px; }
  .contact li { display: flex; align-items: center; gap: 10px; font-size: 10px; margin-bottom: 13px; }
  .contact svg { width: 13px; height: 13px; fill: #fff; flex: none; }
  .offer {
    margin: 22px 12px 0;
    border: 1.5px dashed var(--ink);
    padding: 12px 8px;
    color: var(--orange);
    text-align: left;
  }
  .offer__title { font-size: 19px; font-weight: 700; }
  .offer__date { font-size: 12px; margin-top: 2px; }
  .note { font-size: 12px; line-height: 1.35; padding: 16px 16px 0; }

  /* inside */
  .band-blue {
    background: var(--blue);
    height: 95px;
    flex: none;
    display: flex; align-items: center; justify-content: center;
    color: #222;
    font-weight: 300;
    font-size: 21px;
    line-height: 1.15;
    padding: 0 10px;
  }
  .band-blue--caps { text-transform: uppercase; }
  .inside-body { font-size: 10.5px; line-height: 1.4; padding: 16px 14px 0; color: var(--ink-soft); }
  .inside-body p + p { margin-top: 10px; }
  .highlight { font-weight: 700; font-size: 11px; margin-top: 18px; color: var(--ink); }
  .photo--wide { flex: none; height: 150px; margin: auto 12px 14px; border-radius: 4px; }
</style>
</head>
<body>

<section class="sheet sheet--outside" aria-label="Brochure outside">
  <div class="panel">
    <header class="band-orange brand">
      <div class="brand__name"><span>BRIGHT PATH</span><span class="brand__dot"></span></div>
      <div class="brand__sub">OT SERVICES</div>
    </header>
    <p class="intro">Success in school depends on strong auditory and visual processing skills.</p>
    <p class="intro-lead">Your child can build these skills too!</p>
    <ul class="questions">
      <li>Does your child struggle to learn the ABCs or the aleph bet?</li>
      <li>Does your child know the material, yet perform poorly on tests?</li>
      <li>Does your child find it hard to remember names and dates at school, for tests or in everyday life?</li>
    </ul>
    <div class="photo photo--warm" role="img" aria-label="Photo of a smiling girl holding up a report card"></div>
  </div>

  <div class="panel">
    <div class="photo photo--cool photo--top" role="img" aria-label="Photo of a smiling boy resting his chin on his hands"></div>
    <h2 class="question">How can occupational therapy improve auditory processing?</h2>
    <div class="body">
      <p>Hearing and movement are closely linked in the brain. When the right movement is provided, the ears become more receptive to sound. Targeted movement is a core skill of every occupational therapist.</p>
      <p>Therapy combines movement, auditory processing and visual processing techniques. Where needed, reflex integration is also incorporated.</p>
      <p class="caption">Evidence-based<br>programs only</p>
    </div>
  </div>

  <div class="panel">
    <header class="band-orange">
      <ul class="contact">
        <li><svg viewBox="0 0 24 24" aria-hidden="true"><path d="M6.6 10.8a15 15 0 0 0 6.6 6.6l2.2-2.2c.3-.3.7-.4 1-.2 1.1.4 2.3.6 3.6.6.6 0 1 .4 1 1V20c0 .6-.4 1-1 1A17 17 0 0 1 3 4c0-.6.4-1 1-1h3.5c.6 0 1 .4 1 1 0 1.3.2 2.5.6 3.6.1.3 0 .7-.2 1z"/></svg>(555) 318-0427</li>
        <li><svg viewBox="0 0 24 24" aria-hidden="true"><path d="M2 5h20v14H2z M2 5l10 8 10-8" fill="none" stroke="#fff" stroke-width="2"/></svg>BrightPathOT@example.com</li>
        <li><svg viewBox="0 0 24 24" aria-hidden="true"><path d="M12 3 2 12h3v8h5v-5h4v5h5v-8h3z"/></svg>Dana Morel OTR/L</li>
      </ul>
    </header>
    <div class="offer">
      <div class="offer__title">FREE EVALUATION</div>
      <div class="offer__date">Offer expires: 07/02/2015</div>
    </div>
    <p class="note">Enrollment is limited to children who will benefit from the program.</p>
    <div class="photo photo--warm photo--corner" role="img" aria-label="Photo of a thoughtful boy looking upward"></div>
  </div>
</section>

<section class="sheet sheet--inside" aria-label="Brochure inside">
  <div class="panel">
    <h2 class="band-blue band-blue--caps">Auditory<br>Processing</h2>
    <div class="inside-body">
      <p>Children with auditory processing delays often have difficulty:</p>
      <p>Processing what they hear and/or remembering what they hear.</p>
      <p>This affects learning, especially in the early grades, where spoken information must be understood and remembered, such as the names of figures in the weekly parsha or even classmates' names.</p>
    </div>
    <div class="photo photo--warm photo--small" role="img" aria-label="Photo of a young girl cupping her ear"></div>
  </div>

  <div class="panel">
    <h2 class="band-blue">Visual<br>Processing</h2>
    <div class="inside-body">
      <p>Children with visual processing delays have difficulty processing and/or remembering what they see.</p>
      <p>They may struggle to remember or understand visual information. In the early grades this means learning the ABCs: each letter is a shape whose visual details, name and sound must be remembered.</p>
      <p>Later, it means understanding and retaining notes for a test.</p>
      <p>Many of these children can explain all the material before a test, yet do poorly on the exam itself, because exams are visual.</p>
    </div>
    <div class="photo photo--cool photo--small" role="img" aria-label="Photo of a smiling boy with glasses"></div>
  </div>

  <div class="panel">
    <h2 class="band-blue">Combining visual<br>and<br>Auditory information</h2>
    <div class="inside-body">
      <p>Some children find it hard to connect what they hear with what they see, and vice versa. A child may know a letter's name and recognise its shape, yet be unable to match the two. The same challenge appears, in more advanced forms, in the older grades.</p>
      <p class="highlight">Every program is tailored to the individual child</p>
    </div>
    <div class="photo photo--warm photo--wide" role="img" aria-label="Photo of a group of four cheerful children"></div>
  </div>
</section>

</body>
</html>
```